Birchwood Clover Business Cards

I need a business card with my logo, number, Facebook account, and some information about what I am selling. Green card with logo on the front. 555-218-3946 phone number, @birchwoodclover Facebook, •Orchardgrass Hay •Alfalfa Hay •Mixed Grass Hay , and “Premium Quality Hay” all written on the back.

Target Market(s)

Hay

Contact Information for Business Card

Phone number, Facebook, different types of hay.

Colors
00AB8E
00BBA5
67D7C9
C6EFE9
E9F9F6

```html
<!DOCTYPE html>
<html lang="en">
<head>
<meta charset="utf-8">
<title>Birchwood Clover Business Cards</title>
<link rel="stylesheet" href="https://fonts.googleapis.com/css2?family=Yellowtail&family=Kaushan+Script&family=Arimo:wght@700&family=Nunito+Sans:wght@400;700;800&display=swap">
<style>
  :root {
    --brand-green: #00963f;
    --band-green: #00a447;
    --ink: #111111;
    --paper: #ffffff;
    --backdrop: #c9cbcd;
  }
  * { margin: 0; padding: 0; box-sizing: border-box; }
  html, body {
    width: 1187px;
    height: 1200px;
    overflow: hidden;
    background: var(--backdrop);
  }
  .card {
    position: absolute;
    border-radius: 16px;
    overflow: hidden;
  }
  /* Front */
  .card-front {
    left: 219px; top: 122px;
    width: 751px; height: 430px;
    background: var(--brand-green);
  }
  .front-mark {
    position: absolute;
    left: 50%; top: 127px;
    width: 90px; height: 90px;
    margin-left: -45px;
    border-radius: 50%;
    background: var(--paper);
  }
  .front-name {
    position: absolute;
    left: 0; right: 0; top: 248px;
    text-align: center;
    font-family: "Yellowtail", cursive;
    font-size: 54px;
    line-height: 1;
    color: var(--paper);
  }
  /* Back */
  .card-back {
    left: 214px; top: 644px;
    width: 761px; height: 434px;
    background: var(--paper);
  }
  .back-band {
    position: absolute;
    left: 0; right: 0; bottom: 0;
    height: 12px;
    background: var(--band-green);
  }
  .back-mark {
    position: absolute;
    left: 58px; top: 142px;
    width: 90px; height: 90px;
    border-radius: 50%;
    background: var(--brand-green);
  }
  .business {
    position: absolute;
    left: 178px; top: 138px;
  }
  .business-name {
    font-family: "Yellowtail", cursive;
    font-size: 40px;
    line-height: 44px;
    color: var(--ink);
  }
  .business-phone {
    margin-top: 4px;
    font-family: "Arimo", sans-serif;
    font-weight: 700;
    font-size: 35px;
    line-height: 40px;
    color: var(--ink);
    letter-spacing: 0.3px;
  }
  .business-social {
    display: flex;
    align-items: center;
    gap: 6px;
    margin-top: 8px;
    margin-left: 3px;
    font-family: "Nunito Sans", sans-serif;
    font-size: 20px;
    line-height: 26px;
    color: var(--ink);
    letter-spacing: 0.4px;
  }
  .social-dot {
    width: 24px; height: 24px;
    border-radius: 50%;
    background: var(--brand-green);
    flex: none;
  }
  .business-tagline {
    margin-top: 6px;
    font-family: "Nunito Sans", sans-serif;
    font-weight: 800;
    font-size: 16px;
    line-height: 22px;
    color: var(--ink);
    letter-spacing: 0.8px;
  }
  .seller {
    position: absolute;
    left: 483px; top: 140px;
  }
  .seller-name {
    font-family: "Kaushan Script", cursive;
    font-size: 36px;
    line-height: 44px;
    color: var(--brand-green);
  }
  .products {
    list-style: none;
    margin-top: 8px;
    font-family: "Nunito Sans", sans-serif;
    font-size: 20px;
    color: var(--ink);
    letter-spacing: 0.4px;
  }
  .products li {
    display: flex;
    align-items: center;
    height: 40px;
  }
  .products li::before {
    content: "";
    width: 10px; height: 10px;
    border-radius: 50%;
    background: var(--brand-green);
    margin-right: 8px;
  }
</style>
</head>
<body>
  <section class="card card-front">
    <div class="front-mark"></div>
    <h1 class="front-name">Birchwood Clover</h1>
  </section>

  <section class="card card-back">
    <div class="back-mark"></div>
    <div class="business">
      <p class="business-name">Birchwood Clover</p>
      <p class="business-phone">555-218-3946</p>
      <p class="business-social"><span class="social-dot"></span>@birchwoodclover</p>
      <p class="business-tagline">“Premium Quality Hay”</p>
    </div>
    <div class="seller">
      <p class="seller-name">Dale Morrow</p>
      <ul class="products">
        <li>Orchardgrass Hay</li>
        <li>Alfalfa Hay</li>
        <li>Mixed Grass Hay</li>
      </ul>
    </div>
    <div class="back-band"></div>
  </section>
</body>
</html>
```